Boutique Salon Brand Refresh needs color palette, font, templates.

Lorvu Hair Design is an established hair salon celebrating 10 years in business. We are currently evolving our brand to better reflect who we are today, the clients we serve, and the direction we want to take our business moving forward.
Our goal is to position Lorvu as a refined, modern boutique salon created specifically for “The Lorvu Woman.”
In the past, much of our branding and marketing focused on us—our salon, our space, our services, and our team. Going forward, we want to shift that focus to her: who she is, what she values, how she wants to look and feel, and how Lorvu fits into her life.
We want our brand to communicate expertise and quality without feeling overly luxurious, trendy, intimidating, or impersonal. It should feel polished, sophisticated, warm, approachable, and timeless—a boutique experience designed for women who value beautiful, healthy hair and trusted professional guidance.
As part of this rebrand, we are looking to establish a cohesive visual identity that can be carried consistently across our website, social media, email marketing, print materials, signage, and other client touchpoints.

*** For THIS PROJECT, we are SPECIFICALLY LOOKING for:
- A cohesive brand color palette
- 2–3 complementary fonts for consistent use across our marketing
- 4–5 customizable social media templates that can be used across Instagram and Facebook
A visual direction that feels distinctive to Lorvu and speaks directly to The Lorvu Woman.
The following information provides more detail about The Lorvu Woman, our positioning, brand personality, values, and the overall direction we envision for the next chapter of Lorvu Hair Design.
Lorvu Hair Design
Mendham, NJ USA
lorvuhairstudio.example

--PRIMARY AUDIENCE
The Lorvu woman values quality, consistency, and professional guidance.
She wants to look polished and current without appearing overdone or overly trendy.
She may be managing grey hair, changing texture, thinning, dryness, fading color, or a style that no longer reflects who she is. She wants an expert who understands these concerns and can create a realistic plan.
She is willing to invest in professional services and products when she understands their value.
She does not want to experiment with her appearance.
She wants to feel confident in the person caring for her hair.
Women approximately 45 to 65 years old living in Mendham, Morris County, and surrounding communities.

--COLOR PALETTE
The overall appearance should feel calm, spacious, editorial, and cohesive. The entire visual system should feel more like a refined boutique hotel, skincare brand, or luxury lifestyle publication than a traditional salon advertisement.
When choosing the palette, we want the colors to invoke these feelings.
Represents:
Expertise
Confidence
Timelessness
Professionalism
Calm
Warmth
Cleanliness
Soft luxury
Natural beauty
Warmth
Balance
Subtle sophistication
Consistency

--TYPOGRAPHY
The typography system should feel refined, modern, readable, and timeless.
Recommended usage for each font, size, spacing, etc.

----TEMPLATE IDEAS
**EDUCATIONAL POST
Frequently asked questions
Healthy-hair advice
Healthy Hair Tip
Grey Coverage FAQ
Grey Blending FAQ
Product education
Single-tip graphic
**REVIEWS
Google reviews
Finest in Town recognition/Community awards
Long-term guest relationships
Guest testimonials/satisfaction stories
Referral stories
**ADS
**SALON UPDATES/INFO
Holiday hours
Policy reminder
New guest guide
Consultation invitation
Service spotlight
Seasonal guidance
**ABOUT LORVU
Who we are
What to expect from us
What we can provide
Our expertise
**HIGHLIGHT ICON
Questions
Testimonial
Product
Reminders

TEMPLATE RULES
Use the color palette
Use only the font system
Maintain generous spacing
Limit text
Use consistent margins
Keep calls to action simple
Avoid crowded layouts
Use photography intentionally
Keep every template recognizably Lorvu

Target Market(s)

Women approximately 45 to 65 years old living in Mendham, Morris County, and surrounding communities. She values quality, consistency, and professional guidance. She wants to look polished and current without appearing overdone or overly trendy. She is willing to invest in professional services and products when she understands their value.

Industry/Entity Type

Hair Salon

Font styles to use
Serif
Sans Serif
Script

Requirements
Must have
• We are looking to establish a cohesive visual identity that can be carried consistently across platforms. It should communicate expertise and quality without feeling overly fluffy, trendy, intimidating, or impersonal. I would like to see multiple template ideas. Example- one template for education post, one template for reviews, one for salon information/updates. etc. My main goal here is to simplify social media posts by having designated templates for each post category. WE WILL BE KEEPING OUR ORGINAL LOGO- SO COLOR PALETTE MUST REFLECT THAT.
Nice to have
• Color palette and font sets that reflect the brand. **cohesive visual identity**
Should not have
• Nothing flashy, busy, overly trendy.

```html
<!DOCTYPE html>
<html lang="en">
<head>
<meta charset="utf-8">
<title>Lorvu Hair Design — Fonts &amp; Color Palette</title>
<link rel="stylesheet" href="https://fonts.googleapis.com/css2?family=Bodoni+Moda:wght@400;600&family=Jost:wght@300;400&family=Playfair+Display&family=Parisienne&family=Pathway+Gothic+One&display=swap">
<style>
  :root {
    --ink: #2a2925;
    --taupe: #857665;
    --sand: #d5c7b9;
    --cream: #f1eeeb;
    --cocoa: #6e5443;
    --mist: #e4dfd8;
    --heading: #6b5140;
    --rule: #a39585;
    --paper: #ffffff;
  }
  * { margin: 0; padding: 0; box-sizing: border-box; }
  html, body { width: 1200px; height: 1153px; overflow: hidden; background: var(--paper); }
  .board { position: relative; width: 1200px; height: 1153px; }

  .section-title {
    position: absolute; left: 78px;
    font-family: "Jost", sans-serif; font-weight: 300;
    font-size: 48px; line-height: 1; letter-spacing: 0.48em;
    color: var(--heading);
  }
  .section-title.fonts { top: 115px; }
  .section-title.palette { top: 691px; }

  .specimen {
    position: absolute; text-align: center; transform: translateX(-50%);
    white-space: nowrap;
  }
  .specimen .sample {
    display: block; position: relative; height: 104px; line-height: 104px;
    color: var(--taupe);
  }
  .specimen .name {
    display: block; margin-top: 22px;
    font-family: "Pathway Gothic One", sans-serif; font-size: 31px; line-height: 1;
    color: var(--ink);
  }
  .row-one { top: 196px; }
  .row-two { top: 417px; }

  .sample.bodoni { font-family: "Bodoni Moda", serif; font-weight: 600; font-size: 94px; top: 9px; }
  .sample.bodoni-book { font-family: "Bodoni Moda", serif; font-weight: 600; font-size: 94px; color: var(--cocoa); top: 10px; }
  .sample.neutra-light { font-family: "Jost", sans-serif; font-weight: 300; font-size: 88px; letter-spacing: 0.02em; top: 7px; }
  .sample.neutra-book { font-family: "Jost", sans-serif; font-weight: 400; font-size: 88px; letter-spacing: 0.16em; top: 17px; }
  .sample.playfair { font-family: "Playfair Display", serif; font-size: 118px; top: -6px; }
  .sample.parisienne { font-family: "Parisienne", cursive; font-size: 92px; }
  .small-cap { font-size: 0.76em; }

  .divider { position: absolute; width: 1px; background: var(--rule); }

  .swatch { position: absolute; top: 798px; width: 142px; height: 142px; }
  .hex {
    position: absolute; top: 978px; width: 142px; text-align: center;
    font-family: "Pathway Gothic One", sans-serif; font-size: 24px; line-height: 1;
    color: var(--ink); letter-spacing: 0.01em; margin-left: -6px;
  }
  .c1 { left: 82px; }  .c2 { left: 262px; } .c3 { left: 442px; }
  .c4 { left: 617px; } .c5 { left: 800px; } .c6 { left: 978px; }
</style>
</head>
<body>
<main class="board">
  <h1 class="section-title fonts">FONTS</h1>

  <div class="specimen row-one" style="left:176px">
    <span class="sample bodoni">Abc</span>
    <span class="name">Bodoni bk bt</span>
  </div>
  <div class="divider" style="left:319px; top:214px; height:142px"></div>

  <div class="specimen row-one" style="left:443px">
    <span class="sample neutra-light">A<span class="small-cap">BC</span></span>
    <span class="name">Neutra Light sc alt</span>
  </div>
  <div class="divider" style="left:586px; top:214px; height:142px"></div>

  <div class="specimen row-one" style="left:733px">
    <span class="sample playfair">Abc</span>
    <span class="name">Playfair display regular</span>
  </div>
  <div class="divider" style="left:895px; top:214px; height:142px"></div>

  <div class="specimen row-one" style="left:1010px">
    <span class="sample parisienne">Abc</span>
    <span class="name">Parisiene</span>
  </div>

  <div class="specimen row-two" style="left:441px">
    <span class="sample neutra-book">A<span class="small-cap">BC</span></span>
    <span class="name">Neutra Book sc alt</span>
  </div>
  <div class="divider" style="left:581px; top:434px; height:142px"></div>

  <div class="specimen row-two" style="left:712px">
    <span class="sample bodoni-book">Abc</span>
    <span class="name">Bodoni Bk BT BOOK</span>
  </div>

  <h2 class="section-title palette">COLOR PALLETTE</h2>

  <div class="swatch c1" style="background:var(--ink)"></div>
  <div class="swatch c2" style="background:var(--taupe)"></div>
  <div class="swatch c3" style="background:var(--sand)"></div>
  <div class="swatch c4" style="background:var(--cream)"></div>
  <div class="swatch c5" style="background:var(--cocoa)"></div>
  <div class="swatch c6" style="background:var(--mist)"></div>

  <p class="hex c1">#2A2925</p>
  <p class="hex c2">#857665</p>
  <p class="hex c3">#D5C7B9</p>
  <p class="hex c4">#F1EEEB</p>
  <p class="hex c5">#A38871</p>
  <p class="hex c6">#E4DFD8</p>
</main>
</body>
</html>
```